Kettle Past Noon - Book cover for collection of odd short stories

We need a book cover for ebook and print versions for an anthology of short stories. The title "Kettle Past Noon" relates to stories with something odd or not-quite-right about them. The attached photo is an example of a carpenter level, the idea is the level would appear perfectly level, but the bubble would be off-center. "Stories by: Moira Tesslund, Janet Orloff, Rob T. Vessey, Author, Author". Other creative elements could be wildly improbable things, e.g. pig's flying, hell freezing, etc. We prefer an uncluttered cover, however. Licenses included or unnecessary, delivery files must be fully compatible with Adobe Illustrator, with all layers intact.

Target Market(s)

People who like short stories with odd overtones or twist endings.

Industry/Entity Type

Book Publisher

Font styles to use
Serif

Colors

Designer to choose colors to be used in the design.

Requirements
Must have
• Incorporation of the concept, Kettle Past Noon
Nice to have
• Other ways to show the same meaning

```html
<!DOCTYPE html>
<html lang="en">
<head>
<meta charset="utf-8">
<title>Kettle Past Noon — Book Cover</title>
<link rel="stylesheet" href="https://fonts.googleapis.com/css2?family=EB+Garamond:ital,wght@0,400;0,500;1,400&family=Crimson+Pro:ital,wght@1,400&display=swap">
<style>
  :root {
    --paper: #ffffff;
    --ink: #2b2320;
    --title-brown: #3b0e04;
    --brass-light: #cbb28a;
    --rope: #8c8468;
    --mark-dark: #1a1a1a;
  }
  * { box-sizing: border-box; margin: 0; padding: 0; }
  html, body { width: 1200px; height: 854px; overflow: hidden; background: var(--paper); }
  .cover {
    position: relative;
    width: 1200px;
    height: 854px;
    overflow: hidden;
    background: var(--paper);
    font-family: "EB Garamond", Georgia, serif;
    color: var(--ink);
  }

  /* Back cover */
  .back-copy {
    position: absolute;
    left: 82px;
    width: 440px;
    font-size: 21.5px;
    line-height: 25.6px;
  }
  .back-copy span { display: block; white-space: nowrap; }
  .back-copy--first { top: 88px; }
  .back-copy--second { top: 317px; }
  .back-tagline {
    position: absolute;
    right: 698px;
    top: 570px;
    font-style: italic;
    font-size: 21.5px;
    white-space: nowrap;
  }
  .publisher {
    position: absolute;
    display: flex;
    flex-direction: column;
    align-items: flex-start;
  }
  .publisher--back { left: 37px; top: 707px; }
  .publisher__square {
    width: 83px;
    height: 83px;
    background: var(--mark-dark);
  }
  .publisher__name {
    margin-top: 8px;
    font-size: 15px;
    color: var(--ink);
    white-space: nowrap;
  }
  .publisher--spine { left: 583px; top: 780px; align-items: center; }
  .publisher--spine .publisher__square { width: 30px; height: 30px; }
  .publisher--spine .publisher__name { margin-top: 3px; font-size: 6px; }

  /* Spine */
  .spine-title {
    position: absolute;
    left: 575px;
    top: 40px;
    height: 504px;
    writing-mode: vertical-rl;
    font-size: 48px;
    font-weight: 400;
    line-height: 50px;
    color: var(--title-brown);
    white-space: nowrap;
  }
  .spine-title em { font-style: italic; }
  .spine-rope {
    position: absolute;
    left: 584px;
    top: 552px;
    width: 34px;
    height: 148px;
  }

  /* Front cover */
  .front-art {
    position: absolute;
    left: 678px;
    top: 60px;
    width: 476px;
    height: 330px;
  }
  .front-title {
    position: absolute;
    left: 660px;
    width: 504px;
    top: 400px;
    text-align: center;
    color: var(--title-brown);
    font-size: 80px;
    line-height: 72px;
    font-weight: 500;
    white-space: nowrap;
  }
  .front-title em { font-style: italic; font-weight: 400; }
  .front-byline {
    position: absolute;
    left: 660px;
    width: 504px;
    top: 538px;
    text-align: center;
    font-family: "Crimson Pro", "EB Garamond", Georgia, serif;
    font-style: italic;
    font-weight: 400;
    font-size: 20px;
    line-height: 26px;
    color: var(--ink);
    white-space: nowrap;
  }
</style>
</head>
<body>
<main class="cover">

  <section class="back">
    <p class="back-copy back-copy--first">
      <span>Proin tempor, ligula ut tincidunt tempor, mauris</span>
      <span>nibh feugiat odio, nec tincidunt erat orci dictum</span>
      <span>purus. Etiam luctus odio. Aliquam adipiscing</span>
      <span>urna a felis. Quisque sed elit in eros aliquet</span>
      <span>ultrices. Donec at sem. Vestibulum cursus.</span>
      <span>Integer dolor. Vestibulum sit amet sem nec augue</span>
      <span>fermentum consectetuer. Integer justo.</span>
    </p>
    <p class="back-copy back-copy--second">
      <span>Vivamus vel sapien. Praesent nisl tortor, laoreet</span>
      <span>eu, dapibus quis, egestas non, mauris. Cum sociis</span>
      <span>natoque penatibus et magnis dis parturient</span>
      <span>montes, nascetur ridiculus mus. Nullam eleifend</span>
      <span>pharetra felis. Mauris nibh velit, tristique ac,</span>
      <span>lacinia in, scelerisque et, ante. Donec viverra</span>
      <span>tortor sed nulla. Phasellus nec magna. Aenean</span>
      <span>vehicula, turpis in congue eleifend, mauris lorem</span>
    </p>
    <p class="back-tagline">Vestibulum vel tellus. Sed</p>
    <div class="publisher publisher--back">
      <span class="publisher__square"></span>
      <span class="publisher__name">Stray Lantern Publishers</span>
    </div>
  </section>

  <section class="spine">
    <h2 class="spine-title">KETTLE <em>PAST</em>-NOON</h2>
    <svg class="spine-rope" viewBox="0 0 34 148" role="img" aria-label="Illustration of a frayed plumb-line cord hanging down the spine">
      <rect x="0" y="0" width="34" height="148" rx="6" fill="var(--rope)" opacity="0.35"/>
    </svg>
    <div class="publisher publisher--spine">
      <span class="publisher__square"></span>
      <span class="publisher__name">Stray Lantern</span>
    </div>
  </section>

  <section class="front">
    <svg class="front-art" viewBox="0 0 476 330" role="img" aria-label="Illustration of a brass plumb bob on its cord, tipped over and shattering like a bubble on a white surface">
      <defs>
        <linearGradient id="brassGlow" x1="0" y1="0" x2="1" y2="1">
          <stop offset="0" stop-color="#f6f3ee"/>
          <stop offset="0.45" stop-color="var(--brass-light)"/>
          <stop offset="1" stop-color="#eceef2"/>
        </linearGradient>
      </defs>
      <rect width="476" height="330" fill="url(#brassGlow)"/>
    </svg>
    <h1 class="front-title">KETTLE<br><em>PAST</em>-NOON</h1>
    <p class="front-byline">Stories of the odd and unforgettable by:<br>Moira Tesslund, Janet Orloff, Rob T. Vessey, Author, Author</p>
  </section>

</main>
</body>
</html>
```